Stationery and Business Cards
Multi-Family Interior & Exterior Renovations
Creative Brief
Professional
Rodrigo L Quintero
5817-K Birch Hollow Rd. #629
vexmoregroup@mailbox.example
Need Business Cards for all my employees below and two additional cards for the company principals for our real estate division as described on the Card Back details:
Front:
Rodrigo L. Quintero
President
Phone: 615-902-1486
Email: Rquintero@VexmoreGroup.example
Murfreesboro, TN 37000
www.VexmoreGroup.example
Tomas Delgadillo
Vice-President
Phone: 404-813-6271
Tdelgadillo@VexmoreGroup.example
Julio Serna
Administrative Manager
Phone: 615-274-3059
Email: Jserna@VexmoreGroup.example
Wilbur Kröt
Project Manager
Phone: 615-381-9042
Email: Wkrot@VexmoreGroup.example
Card Back:
Our Services:
Interior Renovations
Exterior Painting
Replacement Windows
Siding Installation
Carpentry Repairs
Step Tread Replacements
Concrete Work
Also need two additional cards for Rodrigo and Tomas with the same Front but with the following back:
**Two Additional Real Estate Cards Back:**
Real Estate Investments
Houses & Apartments For Rent
We Pay All Cash For Properties
Tired Landlord?
REO?
Ugly Houses needing repairs?
Hablamos Español

```html
<!DOCTYPE html>
<html lang="en">
<head>
<meta charset="utf-8">
<title>Vexmore Construction Services Group — Stationery</title>
<link rel="stylesheet" href="https://fonts.googleapis.com/css2?family=Didact+Gothic&family=Open+Sans:ital,wght@0,400;0,600;0,700;1,700&family=Homemade+Apple&display=swap">
<style>
:root{
  --green:#8cc63f;
  --charcoal:#3c3c3c;
  --ink:#4a4a4a;
  --paper:#ffffff;
  --stage:#e8e7e3;
  --logo-font:"Didact Gothic",sans-serif;
  --text-font:"Open Sans",sans-serif;
}
*{box-sizing:border-box;margin:0;padding:0}
html,body{width:1200px;height:608px;overflow:hidden}
body{background:var(--stage);font-family:var(--text-font);color:var(--ink);position:relative}
.piece{position:absolute;background:var(--paper);box-shadow:0 2px 6px rgba(0,0,0,.25);overflow:hidden}
.band{position:absolute;left:0;top:0;width:100%;height:100%}
.wordmark{display:flex;align-items:center;gap:4px}
.wordmark .square{background:var(--green);flex:none}
.wordmark .name{font-family:var(--logo-font);color:var(--ink);line-height:1}
.tagline{color:var(--green);font-family:var(--logo-font);white-space:nowrap}
.white{color:#fff}
.green{color:var(--green)}
.phone-num{position:absolute;color:#fff;font-weight:700;white-space:nowrap;letter-spacing:.3px;line-height:1}
.web{position:absolute;color:var(--charcoal);font-weight:700;white-space:nowrap;line-height:1.1}
.web::after{content:"";display:block;height:1.5px;background:var(--green);margin-top:1px}

/* standalone logo */
.brand-lockup{position:absolute;left:45px;top:22px}
.brand-lockup .square{width:34px;height:34px;background:var(--green)}
.brand-lockup .name{font-size:40px;color:var(--charcoal)}
.brand-lockup .tagline{font-size:7.5px;margin:3px 0 0 38px;color:var(--charcoal);letter-spacing:.4px}

/* business cards */
.card{width:150px;height:86px;left:22px}
.card .wordmark{position:absolute;left:8px;top:8px}
.card .square{width:9px;height:9px}
.card .name{font-size:15px}
.card .tagline{position:absolute;left:21px;top:24px;font-size:4px}
.card .person{position:absolute;left:8px;top:33px;font-size:6.5px;font-weight:700;color:var(--green);line-height:1}
.card .role{display:block;font-size:3.8px;color:var(--ink);font-weight:400;margin-top:1px}
.card .contact{position:absolute;left:8px;top:52px;font-size:3.6px;line-height:1.35;color:#fff}
.card .phone-num{right:6px;top:42px;font-size:7px}
.card .web{right:7px;bottom:3px;font-size:4.2px}

/* letterhead */
.letterhead{left:200px;top:70px;width:335px;height:428px}
.letterhead .wordmark{position:absolute;left:34px;top:30px}
.letterhead .square{width:18px;height:18px}
.letterhead .name{font-size:30px}
.letterhead .tagline{position:absolute;left:56px;top:60px;font-size:5.5px}
.letter{position:absolute;left:34px;top:96px;width:268px;font-size:5.6px;line-height:1.5;color:#555}
.letter p{margin-bottom:7px}
.signature{font-family:"Homemade Apple",cursive;font-size:10px;color:#666;margin-top:4px}
.letterhead .footer-info{position:absolute;left:22px;bottom:16px;font-size:4.6px;line-height:1.4;color:#fff}
.letterhead .phone-num{right:22px;bottom:44px;font-size:11px}
.letterhead .web{right:22px;bottom:8px;font-size:7px}
.letterhead .phone-icon{position:absolute;right:58px;bottom:62px;width:18px;height:18px}

/* card backs */
.card-back{top:506px;width:162px;height:92px}
.card-back .photo{position:absolute;left:0;top:0;width:100%;height:36px;background:linear-gradient(100deg,#2f5f8a 0%,#7fa6c6 40%,#c9c0ae 70%,#8e8a80 100%)}
.card-back .photo-title{position:absolute;left:8px;top:4px;color:#fff;font-size:7px;line-height:1;font-weight:600}
.card-back .photo-title small{display:block;color:var(--green);font-size:3.5px;margin-top:1px}
.card-back .strip-label{position:absolute;left:8px;top:40px;font-size:6.5px;font-weight:700;color:var(--green)}
.card-back ul{position:absolute;left:8px;top:53px;list-style:none;font-size:3.4px;line-height:1.38;color:#444}
.card-back li::before{content:"";display:inline-block;width:2px;height:2px;background:var(--green);margin-right:2px;vertical-align:middle}
.card-back .wordmark{position:absolute;right:8px;top:60px}
.card-back .square{width:8px;height:8px}
.card-back .name{font-size:13px}
.card-back .tagline{position:absolute;right:8px;top:76px;font-size:3.6px}

/* fax sheet */
.fax{left:550px;top:22px;width:218px;height:282px}
.fax .wordmark{position:absolute;left:16px;top:16px}
.fax .square{width:11px;height:11px}
.fax .name{font-size:18px}
.fax .tagline{position:absolute;left:31px;top:36px;font-size:4px}
.fax-title{position:absolute;right:16px;top:44px;font-size:12px;font-weight:700;font-style:italic;color:var(--green)}
.fax-box{position:absolute;left:16px;right:16px;top:64px;height:86px;border:1px solid #aaa;padding:6px 8px}
.fax-row{display:flex;font-size:5.5px;color:#333;height:13px;align-items:flex-end;border-bottom:.75px solid #999;padding-bottom:1px}
.fax-checks{display:flex;flex-wrap:wrap;gap:3px 8px;margin-top:7px;font-size:5.5px;color:#333}
.fax-checks span::before{content:"";display:inline-block;width:5px;height:5px;border:.75px solid #333;margin-right:2px;vertical-align:-1px}
.fax .phone-num{right:16px;bottom:32px;font-size:9px}
.fax .web{right:16px;bottom:7px;font-size:6px}
.fax .phone-icon{position:absolute;right:48px;bottom:44px;width:15px;height:15px}

/* envelopes */
.envelope{left:782px;width:400px;height:148px}
.envelope-back{top:14px}
.envelope-back .flap-mark{position:absolute;left:168px;top:14px;color:#fff;font-family:var(--logo-font);font-size:14px}
.envelope-front{top:172px}
.envelope-front .wordmark{position:absolute;left:16px;top:16px}
.envelope-front .square{width:14px;height:14px}
.envelope-front .name{font-size:24px}
.envelope-front .tagline{position:absolute;left:34px;top:44px;font-size:4.6px}
.envelope-front .return{position:absolute;left:18px;top:108px;font-size:5px;line-height:1.35;color:#fff}
.envelope-front .web{right:24px;bottom:6px;font-size:6px}

/* folder */
.folder-inside{left:555px;top:320px;width:310px;height:280px;background:var(--charcoal)}
.folder-inside .wordmark{position:absolute;left:26px;top:168px}
.folder-inside .square{width:16px;height:16px}
.folder-inside .name{font-size:26px;color:#fff}
.folder-inside .tagline{position:absolute;left:46px;top:197px;font-size:5px}
.folder-inside .details{position:absolute;left:28px;top:210px;font-size:5.6px;line-height:1.35;color:#fff}
.folder-inside .details .green{display:block}
.folder-front{left:868px;top:320px;width:314px;height:280px}
.folder-front .wordmark{position:absolute;left:50px;top:70px}
.folder-front .square{width:26px;height:26px}
.folder-front .name{font-size:42px}
.folder-front .tagline{position:absolute;left:82px;top:114px;font-size:8px}
.folder-front .phone-num{left:96px;top:174px;font-size:18px}
.folder-front .web{left:126px;top:212px;font-size:10px}
.folder-front .phone-icon{position:absolute;left:152px;top:134px;width:32px;height:32px}
.hidden-defs{position:absolute;width:0;height:0}
</style>
</head>
<body>

<svg class="hidden-defs" aria-hidden="true">
  <defs>
    <symbol id="phone-badge" viewBox="0 0 24 24">
      <circle cx="12" cy="12" r="12" fill="#8cc63f"/>
      <circle cx="12" cy="12" r="10.3" fill="none" stroke="#fff" stroke-width="1"/>
      <path d="M5 10c0-3.6 14-3.6 14 0v1.6h-3.4V10.2c-1.8-.7-5.4-.7-7.2 0v1.4H5z" fill="#fff"/>
      <path d="M8 12.2h8l2 5.6H6z" fill="#fff"/>
      <circle cx="12" cy="15" r="1.6" fill="#8cc63f"/>
    </symbol>
  </defs>
</svg>

<div class="brand-lockup">
  <div class="wordmark"><span class="square"></span><span class="name">Vexmore</span></div>
  <div class="tagline">Construction Services Group</div>
</div>

<!-- business cards -->
<div class="piece card" style="top:120px">
  <svg class="band" viewBox="0 0 150 86" aria-hidden="true">
    <path d="M0 45H90L98 34H150" fill="none" stroke="#8cc63f" stroke-width="1.2"/>
    <path d="M0 48H90L98 37H150V70H80L72 78H0Z" fill="#3c3c3c"/>
    <use href="#phone-badge" x="111" y="22" width="12" height="12"/>
  </svg>
  <div class="wordmark"><span class="square"></span><span class="name">Vexmore</span></div>
  <div class="tagline">Construction Services Group</div>
  <div class="person">Rodrigo L. Quintero<span class="role">President</span></div>
  <div class="contact">5817-K Birch Hollow Rd. #629<br>Murfreesboro, TN 37000<br>866-555-0142<br>Rquintero@VexmoreGroup.example</div>
  <div class="phone-num">615-902-1486</div>
  <div class="web">www.VexmoreGroup.example</div>
</div>

<div class="piece card" style="top:213px">
  <svg class="band" viewBox="0 0 150 86" aria-hidden="true">
    <path d="M0 45H90L98 34H150" fill="none" stroke="#8cc63f" stroke-width="1.2"/>
    <path d="M0 48H90L98 37H150V70H80L72 78H0Z" fill="#3c3c3c"/>
    <use href="#phone-badge" x="111" y="22" width="12" height="12"/>
  </svg>
  <div class="wordmark"><span class="square"></span><span class="name">Vexmore</span></div>
  <div class="tagline">Construction Services Group</div>
  <div class="person">Wilbur Kröt<span class="role">Project Manager</span></div>
  <div class="contact">5817-K Birch Hollow Rd. #629<br>Murfreesboro, TN 37000<br>866-555-0142<br>Wkrot@VexmoreGroup.example</div>
  <div class="phone-num">615-381-9042</div>
  <div class="web">www.VexmoreGroup.example</div>
</div>

<div class="piece card" style="top:306px">
  <svg class="band" viewBox="0 0 150 86" aria-hidden="true">
    <path d="M0 45H90L98 34H150" fill="none" stroke="#8cc63f" stroke-width="1.2"/>
    <path d="M0 48H90L98 37H150V70H80L72 78H0Z" fill="#3c3c3c"/>
    <use href="#phone-badge" x="111" y="22" width="12" height="12"/>
  </svg>
  <div class="wordmark"><span class="square"></span><span class="name">Vexmore</span></div>
  <div class="tagline">Construction Services Group</div>
  <div class="person">Tomas Delgadillo<span class="role">Vice-President</span></div>
  <div class="contact">5817-K Birch Hollow Rd. #629<br>Murfreesboro, TN 37000<br>866-555-0142<br>Tdelgadillo@VexmoreGroup.example</div>
  <div class="phone-num">404-813-6271</div>
  <div class="web">www.VexmoreGroup.example</div>
</div>

<div class="piece card" style="top:399px">
  <svg class="band" viewBox="0 0 150 86" aria-hidden="true">
    <path d="M0 45H90L98 34H150" fill="none" stroke="#8cc63f" stroke-width="1.2"/>
    <path d="M0 48H90L98 37H150V70H80L72 78H0Z" fill="#3c3c3c"/>
    <use href="#phone-badge" x="111" y="22" width="12" height="12"/>
  </svg>
  <div class="wordmark"><span class="square"></span><span class="name">Vexmore</span></div>
  <div class="tagline">Construction Services Group</div>
  <div class="person">Julio Serna<span class="role">Administrative Manager</span></div>
  <div class="contact">5817-K Birch Hollow Rd. #629<br>Murfreesboro, TN 37000<br>866-555-0142<br>Jserna@VexmoreGroup.example</div>
  <div class="phone-num">615-274-3059</div>
  <div class="web">www.VexmoreGroup.example</div>
</div>

<!-- letterhead -->
<div class="piece letterhead">
  <svg class="band" viewBox="0 0 335 428" aria-hidden="true">
    <path d="M0 372H205L218 356H335" fill="none" stroke="#8cc63f" stroke-width="1.5"/>
    <path d="M0 376H205L218 360H335V398H180L168 412H0Z" fill="#3c3c3c"/>
  </svg>
  <div class="wordmark"><span class="square"></span><span class="name">Vexmore</span></div>
  <div class="tagline">Construction Services Group</div>
  <div class="letter">
    <p>Ms. Dana Whitlock<br>Customer Service Manager<br>Norvale Inc.<br>480 Ledger Blvd.<br>Fairhill, CO 80000</p>
    <p>Dear Ms. Whitlock:</p>
    <p>I was excited to see your opening for a customer service rep, and I hope to be invited for an interview.</p>
    <p>My background includes serving as a customer service associate within both call-center and retail environments. Most recently, I worked on the customer service desk for ValueBarn, where my responsibilities included handling customer merchandise returns, issuing refunds/store credits, flagging damaged merchandise for shipment back to vendors and providing back-up cashiering during busy periods.</p>
    <p>Previously, I worked within two high-volume customer-support call centers for a major telecommunications carrier and a satellite television services provider. In these positions, I demonstrated the ability to resolve a variety of issues and complaints (such as billing disputes, service interruptions or cutoffs, repair technician delays/no-shows and equipment malfunctions). I consistently met my call-volume goals, handling an average of 56 to 60 calls per day.</p>
    <p>In addition to this experience, I gained considerable customer service skills during my part-time employment as a waitress and restaurant hostess while in high school.</p>
    <p>Sincerely,</p>
    <div class="signature">Hollis Brandt</div>
  </div>
  <svg class="phone-icon" viewBox="0 0 24 24" aria-hidden="true"><use href="#phone-badge"/></svg>
  <div class="phone-num">615-902-1486</div>
  <div class="footer-info">5817-K Birch Hollow Rd. #629, Murfreesboro, TN 37000<br>866-555-0142<br>Rquintero@VexmoreGroup.example</div>
  <div class="web">www.VexmoreGroup.example</div>
</div>

<!-- card backs -->
<div class="piece card-back" style="left:200px">
  <div class="photo" role="img" aria-label="Photo of renovated multi-family apartment buildings under a blue sky"></div>
  <div class="photo-title">Multi-Family<br>Renovation<small>www.VexmoreGroup.example</small></div>
  <svg class="band" viewBox="0 0 162 92" aria-hidden="true">
    <path d="M0 36H162V44H70L62 51H0Z" fill="#3c3c3c"/>
    <path d="M62 51L70 44H162V49H72L66 54H0V51Z" fill="#8cc63f"/>
  </svg>
  <div class="strip-label">Our Services:</div>
  <ul>
    <li>Interior Renovations</li><li>Exterior Painting</li><li>Replacement Windows</li><li>Siding Installation</li><li>Carpentry Repairs</li><li>Step Tread Replacements</li><li>Concrete Work</li>
  </ul>
  <div class="wordmark"><span class="square"></span><span class="name">Vexmore</span></div>
  <div class="tagline">Construction Services Group</div>
</div>

<div class="piece card-back" style="left:370px">
  <div class="photo" role="img" aria-label="Photo of apartment buildings available as real estate investments"></div>
  <div class="photo-title">Real Estate<br>Investments<small>www.VexmoreGroup.example</small></div>
  <svg class="band" viewBox="0 0 162 92" aria-hidden="true">
    <path d="M0 36H162V44H70L62 51H0Z" fill="#3c3c3c"/>
    <path d="M62 51L70 44H162V49H72L66 54H0V51Z" fill="#8cc63f"/>
  </svg>
  <div class="strip-label">Call Us Today!</div>
  <ul>
    <li>Real Estate Investments</li><li>Houses &amp; Apartments For Rent</li><li>We Pay All Cash For Properties</li><li>Tired Landlord?</li><li>REO?</li><li>Ugly Houses needing repairs?</li><li>Hablamos Español</li>
  </ul>
  <div class="wordmark"><span class="square"></span><span class="name">Vexmore</span></div>
  <div class="tagline">Construction Services Group</div>
</div>

<!-- fax sheet -->
<div class="piece fax">
  <svg class="band" viewBox="0 0 218 282" aria-hidden="true">
    <path d="M0 240H118L128 228H218" fill="none" stroke="#8cc63f" stroke-width="1.2"/>
    <path d="M0 243H118L128 231H218V258H92L82 268H0Z" fill="#3c3c3c"/>
  </svg>
  <div class="wordmark"><span class="square"></span><span class="name">Vexmore</span></div>
  <div class="tagline">Construction Services Group</div>
  <div class="fax-title">Fax Sheet</div>
  <div class="fax-box">
    <div class="fax-row">FROM:</div>
    <div class="fax-row">PAGES:</div>
    <div class="fax-row">DATE:</div>
    <div class="fax-row">CC:</div>
    <div class="fax-checks"><span>Urgent</span><span>For Review</span><span>Please Comment</span><span>Please Reply</span><span>Please Recycle</span></div>
  </div>
  <svg class="phone-icon" viewBox="0 0 24 24" aria-hidden="true"><use href="#phone-badge"/></svg>
  <div class="phone-num">615-902-1486</div>
  <div class="web">www.VexmoreGroup.example</div>
</div>

<!-- envelope back -->
<div class="piece envelope envelope-back">
  <svg class="band" viewBox="0 0 400 148" aria-hidden="true">
    <path d="M0 0H400V6C360 60 300 70 200 96C100 70 40 60 0 6Z" fill="#8cc63f"/>
    <path d="M0 6C40 60 100 70 200 96C300 70 360 60 400 6" fill="none" stroke="#3c3c3c" stroke-width="2"/>
  </svg>
  <div class="flap-mark">Vexmore</div>
</div>

<!-- envelope front -->
<div class="piece envelope envelope-front">
  <svg class="band" viewBox="0 0 400 148" aria-hidden="true">
    <path d="M0 98H240L250 92H400" fill="none" stroke="#8cc63f" stroke-width="1.5"/>
    <path d="M0 101H240L250 95H400V126H270L258 134H0Z" fill="#3c3c3c"/>
  </svg>
  <div class="wordmark"><span class="square"></span><span class="name">Vexmore</span></div>
  <div class="tagline">Construction Services Group</div>
  <div class="return">5817-K Birch Hollow Rd. #629<br>Murfreesboro, TN 37000</div>
  <div class="web">www.VexmoreGroup.example</div>
</div>

<!-- folder inside -->
<div class="piece folder-inside">
  <svg class="band" viewBox="0 0 310 280" aria-hidden="true">
    <path d="M0 258L300 236L310 280H0Z" fill="#8cc63f"/>
  </svg>
  <div class="wordmark"><span class="square"></span><span class="name">Vexmore</span></div>
  <div class="tagline">Construction Services Group</div>
  <div class="details">5817-K Birch Hollow Rd. #629<br>Murfreesboro, TN 37000<br>866-555-0142<br>Rquintero@VexmoreGroup.example<span class="green">www.VexmoreGroup.example</span></div>
</div>

<!-- folder front -->
<div class="piece folder-front">
  <svg class="band" viewBox="0 0 314 280" aria-hidden="true">
    <path d="M0 158H80L90 148H314" fill="none" stroke="#8cc63f" stroke-width="2"/>
    <path d="M0 162H80L90 152H314V196H110L98 208H0Z" fill="#3c3c3c"/>
    <path d="M0 236H314V280H0Z" fill="#8cc63f"/>
  </svg>
  <div class="wordmark"><span class="square"></span><span class="name">Vexmore</span></div>
  <div class="tagline">Construction Services Group</div>
  <svg class="phone-icon" viewBox="0 0 24 24" aria-hidden="true"><use href="#phone-badge"/></svg>
  <div class="phone-num">615-902-1486</div>
  <div class="web">www.VexmoreGroup.example</div>
</div>

</body>
</html>
```